Buch-/E-Book-Cover für Autobiografie
Zielgruppe
Ich bin Autor und habe soeben meine Autobiografie verfasst. Sie handelt hauptsächlich von meiner Flagfootball Karriere und meinem Weg vom American Football Fan zum Flagfootball Weltmeister.
Ich benötige ein Design für das Cover des Buches im DIN A5 Format. Es sollte sehr edel aussehen.
Buchtitel: Nachtfalke
Untertitel: Mein Weg vom ersten Wurf zum Weltmeistertitel im Flagfootball
Aufgabenstellung
Auf der Vorderseite sollte eines der mitgeschickten Bilder, der Titel, der Untertitel des Buches und mein Name stehen. Egal, welches Foto für die Vorderseite ausgewählt wird, der Football sollte jedenfalls gut erkennbar sein.
Auf der Rückseite eine Buchbeschreibung und drei kurze Statements von Testimonials.
Auf dem Buchrücken mein Name und der Buchtitel (ohne Untertitel).
Farblich sollte sich das Design an den Farben meiner Website anlehnen (Hauptfarben Gold, Weiss, Schwarz)

```html
<!DOCTYPE html>
<html lang="de">
<head>
<meta charset="utf-8">
<title>Nachtfalke – Buchcover</title>
<link rel="stylesheet" href="https://fonts.googleapis.com/css2?family=Jost:wght@400&family=Oswald:wght@300;400;500;700&display=swap">
<style>
  :root {
    --gold: #e3bb52;
    --black: #0a0a0a;
    --white: #ffffff;
    --ink: #1a1a1a;
    --leaf-dark: #3d4a2e;
    --leaf-mid: #6f7d52;
    --sky: #c9cfc4;
    --shirt: #15171c;
  }
  html, body {
    margin: 0;
    padding: 0;
    width: 1200px;
    height: 810px;
    overflow: hidden;
    background: var(--white);
  }
  .cover {
    position: relative;
    width: 1200px;
    height: 810px;
    display: flex;
  }

  /* Back cover */
  .back {
    position: relative;
    width: 571px;
    height: 100%;
    background: var(--gold);
    overflow: hidden;
  }
  .back-title {
    position: absolute;
    left: 52px;
    top: 42px;
    margin: 0;
    font-family: "Oswald", sans-serif;
    font-weight: 700;
    font-size: 84px;
    line-height: 1;
    letter-spacing: 1px;
    color: var(--black);
    white-space: nowrap;
  }
  .back-subtitle {
    position: absolute;
    left: 50px;
    top: 152px;
    margin: 0;
    font-family: "Oswald", sans-serif;
    font-weight: 400;
    font-size: 27px;
    line-height: 32px;
    letter-spacing: -0.3px;
    color: var(--white);
    text-transform: uppercase;
    white-space: nowrap;
  }
  .author-portrait {
    position: absolute;
    left: 49px;
    top: 244px;
    width: 213px;
    height: 283px;
    background: linear-gradient(180deg, #e6e4df 0%, #dcdad4 40%, #c9c7c1 100%);
  }
  .motto {
    position: absolute;
    left: 60px;
    top: 533px;
    margin: 0;
    font-family: "Oswald", sans-serif;
    font-weight: 500;
    font-style: italic;
    font-size: 32px;
    line-height: 1.2;
    color: var(--white);
    white-space: nowrap;
  }
  .blurb {
    position: absolute;
    left: 285px;
    top: 242px;
    width: 236px;
    font-family: "Jost", sans-serif;
    font-weight: 400;
    font-size: 13px;
    line-height: 17.8px;
    color: var(--ink);
  }
  .blurb p { margin: 0 0 17.8px; }

  /* Spine */
  .spine {
    position: relative;
    width: 57px;
    height: 100%;
    background: var(--black);
    overflow: hidden;
  }
  .spine-title, .spine-author {
    position: absolute;
    left: 50%;
    writing-mode: vertical-rl;
    transform: translateX(-50%) rotate(180deg);
    margin: 0;
    white-space: nowrap;
    line-height: 1;
  }
  .spine-title {
    top: 218px;
    font-family: "Oswald", sans-serif;
    font-weight: 700;
    font-size: 32px;
    letter-spacing: 0.5px;
    color: var(--gold);
  }
  .spine-author {
    top: 458px;
    font-family: "Oswald", sans-serif;
    font-weight: 300;
    font-size: 21px;
    letter-spacing: 6px;
    color: var(--white);
  }

  /* Front cover */
  .front {
    position: relative;
    flex: 1;
    height: 100%;
    overflow: hidden;
  }
  .front-photo {
    position: absolute;
    inset: 0;
    background:
      radial-gradient(ellipse 30% 20% at 10% 3%, var(--sky) 0%, transparent 70%),
      linear-gradient(90deg, transparent 0%, transparent 48%, rgba(21,23,28,0.85) 62%, rgba(21,23,28,0.9) 100%),
      linear-gradient(160deg, var(--leaf-mid) 0%, var(--leaf-dark) 60%, #2e3823 100%);
  }
  .front-title {
    position: absolute;
    left: 52px;
    top: 42px;
    margin: 0;
    font-family: "Oswald", sans-serif;
    font-weight: 700;
    font-size: 84px;
    line-height: 1;
    letter-spacing: 1px;
    color: var(--gold);
    white-space: nowrap;
  }
  .front-subtitle {
    position: absolute;
    left: 50px;
    top: 220px;
    margin: 0;
    font-family: "Oswald", sans-serif;
    font-weight: 400;
    font-size: 27px;
    line-height: 31px;
    letter-spacing: -0.3px;
    color: var(--white);
    text-transform: uppercase;
    white-space: nowrap;
  }
  .front-author {
    position: absolute;
    left: 52px;
    top: 700px;
    margin: 0;
    font-family: "Oswald", sans-serif;
    font-weight: 400;
    font-size: 56px;
    line-height: 1;
    letter-spacing: 10px;
    color: var(--white);
    white-space: nowrap;
  }
</style>
</head>
<body>
<main class="cover">
  <section class="back">
    <h2 class="back-title">NACHTFALKE</h2>
    <p class="back-subtitle">Mein Weg vom ersten Wurf<br>zum Flagfootball Weltmeistertitel</p>
    <div class="author-portrait" role="img" aria-label="Porträtfoto des Autors im dunklen Trikot mit Football vor heller Wand"></div>
    <p class="motto">“GO FOR GOLD”</p>
    <div class="blurb">
      <p>In meiner Autobiografie erzähle ich die spannende und einzigartige Geschichte, wie ich vom American Football Fan zum Flagfootball Weltmeister wurde. Motiviert durch das Verfolgen der Nordliga und einem zufälligen Treffen mit meinem großen Sportidol, wuchs in mir der Wunsch, selbst am Spielfeld zu stehen und Erfolge zu feiern. Doch wo sollte ich anfangen? Am besten bei null, denn ich hatte nie zuvor Flagfootball gespielt.</p>
      <p>Auf unterhaltsame und lustige Weise tauche ich in den Beginn meiner Reise in den frühen 2000er Jahren ein. Das Ziel fest vor Augen, gründete ich den ersten steirischen Flagfootball Verein und startete meinen Weg der mich bis zur Weltmeisterschaft führte, wo ich als Quarterback mit der österreichischen Nationalmannschaft den Titel holte.</p>
      <p>Begleite mich durch meine Geschichte und erlebe mit mir Höhen und Tiefen, Erfolge und Rückschläge und meinen größten Triumph.</p>
    </div>
  </section>

  <section class="spine">
    <p class="spine-title">NACHTFALKE</p>
    <p class="spine-author">KONRAD WIEBKE</p>
  </section>

  <section class="front">
    <div class="front-photo" role="img" aria-label="Foto des lächelnden Autors im schwarzen Trikot mit Nummer 9, der einen Football hält, vor grünen Bäumen"></div>
    <h1 class="front-title">NACHTFALKE</h1>
    <p class="front-subtitle">Mein Weg vom ersten<br>Wurf zum Flagfootball<br>Weltmeistertitel</p>
    <p class="front-author">KONRAD WIEBKE</p>
  </section>
</main>
</body>
</html>
```